Book cover needed for self help business book

Book cover needed and I will provide back cover blurb and barcode to the winning designer. Book may be too small for spine, but I will give you the page number details to confirm. Book information below:

Title: Nine Winters a Trader
Subtitle: Proven Market Methods That Keep Paying Off Now
Author: Maribel Okonte

Design should be clean, modern, and bold—something that appeals to everyday entrepreneurs and resellers. The cover should reflect grit, real-world hustle, and long-term wisdom without looking overly corporate or flashy. I am open to your creative ideas.

I am open to modern designs, but also designs of rugged old covers that simulate a book that may have aged over the years.

I prefer not to have pictures or silhouettes of people

Requirements
Nice to have
• I am open to modern designs, but also designs of rugged old covers that simulate a book that may have aged over the years.
Should not have
• Pictures or silhouettes of people

```html
<!DOCTYPE html>
<html lang="en">
<head>
<meta charset="UTF-8">
<title>Nine Winters a Trader — Book Cover</title>
<link rel="stylesheet" href="https://fonts.googleapis.com/css2?family=Alfa+Slab+One&family=Archivo+Black&family=Oswald:wght@500&display=swap">
<style>
  :root {
    --page-bg: #ffffff;
    --marble-light: #ecebf1;
    --marble-mid: #dedde6;
    --ink: #2a2a2d;
    --green: #15883d;
    --green-dark: #0b4f22;
    --orange: #ec520f;
    --divider: #8a8a90;
    --stone-warm: #d9c6b4;
    --stone-grey: #8e9088;
    --wood: #c9a186;
    --counter-white: #ece7e1;
  }
  * { margin: 0; padding: 0; box-sizing: border-box; }
  html, body {
    width: 1200px;
    height: 1200px;
    overflow: hidden;
    background: var(--page-bg);
  }
  .cover {
    position: absolute;
    left: 240px;
    top: 60px;
    width: 720px;
    height: 1080px;
    overflow: hidden;
    background:
      radial-gradient(ellipse at 20% 15%, rgba(255,255,255,0.7), transparent 55%),
      radial-gradient(ellipse at 85% 70%, rgba(255,255,255,0.5), transparent 50%),
      linear-gradient(160deg, var(--marble-light), var(--marble-mid) 60%, var(--marble-light));
  }
  .materials-photo {
    position: absolute;
    left: 18px;
    top: 298px;
    width: 682px;
    height: 684px;
    transform: rotate(-2deg);
    background:
      radial-gradient(ellipse at 28% 58%, var(--stone-grey), transparent 45%),
      radial-gradient(ellipse at 62% 52%, var(--stone-warm), transparent 50%),
      radial-gradient(ellipse at 80% 85%, var(--counter-white), transparent 45%),
      radial-gradient(ellipse at 15% 90%, var(--wood), transparent 40%),
      linear-gradient(180deg, #cdbfb1 0%, var(--stone-warm) 45%, #d7cbbd 100%);
    box-shadow: 4px 6px 10px rgba(0,0,0,0.25);
  }
  .line {
    position: absolute;
    left: 0;
    width: 100%;
    text-align: center;
    line-height: 1;
    white-space: nowrap;
  }
  .title-top {
    top: 28px;
    font-family: "Archivo Black", sans-serif;
    font-size: 86px;
    color: var(--ink);
    letter-spacing: -1px;
  }
  .title-bottom {
    top: 100px;
    font-family: "Alfa Slab One", serif;
    font-size: 110px;
    color: var(--green);
    -webkit-text-stroke: 1.5px var(--green-dark);
  }
  .divider {
    position: absolute;
    left: 256px;
    top: 262px;
    width: 208px;
    height: 8px;
  }
  .subtitle-lead {
    top: 266px;
    font-family: "Archivo Black", sans-serif;
    font-size: 74px;
    color: var(--ink);
  }
  .subtitle-key {
    top: 334px;
    font-family: "Archivo Black", sans-serif;
    font-size: 110px;
    color: var(--orange);
    letter-spacing: 1px;
  }
  .subtitle-second {
    top: 438px;
    font-family: "Archivo Black", sans-serif;
    font-size: 80px;
    color: var(--orange);
    letter-spacing: 1px;
  }
  .subtitle-tail {
    top: 506px;
    font-family: "Archivo Black", sans-serif;
  }
  .subtitle-tail .connector { font-size: 24px; color: var(--ink); margin-right: 10px; }
  .subtitle-tail .emphasis { font-size: 42px; font-style: italic; color: var(--green); }
  .author {
    top: 972px;
    font-family: "Oswald", sans-serif;
    font-weight: 500;
    font-size: 64px;
    font-variant: small-caps;
    color: var(--ink);
    letter-spacing: 1px;
  }
</style>
</head>
<body>
  <div class="cover">
    <div class="materials-photo" role="img" aria-label="Photo of renovation material samples: marble, quartz and wood slabs, cabinet hardware and a banded stack of banknotes on a countertop"></div>

    <div class="line title-top">Nine Winters</div>
    <div class="line title-bottom">a Trader</div>

    <svg class="divider" viewBox="0 0 208 8" aria-hidden="true">
      <polygon points="0,8 104,0 208,8" fill="var(--divider)"/>
    </svg>

    <div class="line subtitle-lead">Proven</div>
    <div class="line subtitle-key">MARKET</div>
    <div class="line subtitle-second">METHODS</div>
    <div class="line subtitle-tail"><span class="connector">that</span><span class="emphasis">Keep Paying Off Now</span></div>

    <div class="line author">Maribel Okonte</div>
  </div>
</body>
</html>
```